依頼詳細
今回は、トップページデザインの募集になります。
レスポンシブデザインのサイトで、bootstrap4を利用しコーディングする予定になります。
デザイン幅は2000px、コンテンツの幅はbootstrap4デフォルトの1110pxを基準としてください。ただし最近のデザインの流行を取りいれて、フルワイドや、1200~15000px程度の幅のコンテンツをバランスよくレイアウトしてください。
コンテンツ配置は基本12分割になります。がデザインによっては、多少逸脱してもかまいません。
念のため、サンプルのPSDデータを添付しますので、参照ください。

本文のフォントはゴシック系は游ゴシック、メイリオ、明朝系は遊明朝でお願いします。
飾り文字はフリーフォントか、googleフォントを利用してください。

メイン画像部分・グローバルメニューは、ワイド適用でお願いします。

その他内容詳細に関しては、別添のExcel資料を参照してください。
不明点、質問などありましたらメッセージ等でご連絡ください。
ページ数
1ページ
希望イメージ
シンプル 複雑
単色 カラフル
暗い 明るい
日常 高級
遊び心 厳粛
未来的 伝統的
女性的 男性的
希望する色
黄・オレンジ系、グレー系
納品ファイル
• 高解像度JPG (.jpg)
• フォトショップ形式 (.psd)
補足説明
納品ファイルは、PDF及びクライアント表示確認用のJPGを準備お願いします。
※9月13日追記
本件クライアントのご提案選定に時間を要しておりまして、止むを得ず案件の期間を延長させていただきました。
デザイナー様各位にはご心配をお掛けしすみませんが、案件に問題はございませんのでご安心いただければと思います。
引き続き、どうぞ宜しくお願いいたします。

カラーや素材の入れ方が良かったです。

本件クライアントの確認に時間が掛かってしまいましたが、最終的にカラーや素材の使い方が良かったとのことで、mina-teru様を当選とさせていただきました。
皆様ご提案ありがとうございました。
今後ともどうぞ宜しくお願いいたします。

```html
<!DOCTYPE html>
<html lang="ja">
<head>
<meta charset="utf-8">
<title>森田スポーツ | レスリング用品専門店</title>
<link href="https://fonts.googleapis.com/css2?family=Noto+Sans+JP:wght@400;500;700;900&family=Oswald:wght@500;700&display=swap" rel="stylesheet">
<style>
:root{
  --yellow:#f6c400;
  --black:#111;
  --dark:#222;
  --gray:#3a3a3a;
  --white:#fff;
  --red:#d41a1a;
  --text:#333;
  --photo-red:#b8454a;
  --photo-blue:#4a5a9a;
  --photo-light:#d9d9d9;
}
*{margin:0;padding:0;box-sizing:border-box}
html,body{width:730px;height:1200px;overflow:hidden}
body{font-family:"Noto Sans JP",sans-serif;color:var(--text);background:var(--white);font-size:8px;position:relative}

/* header */
.site-header{position:absolute;top:0;left:0;width:730px;height:48px;background:var(--black)}
.header-topline{position:absolute;top:2px;left:10px;color:#aaa;font-size:5px}
.brand{position:absolute;top:10px;left:12px;display:flex;align-items:center;gap:5px}
.brand-dot{width:12px;height:12px;border-radius:50%;background:var(--yellow)}
.brand-name{color:var(--yellow);font-weight:700;font-size:13px;line-height:1}
.brand-sub{position:absolute;top:28px;left:29px;color:#ccc;font-size:5px;letter-spacing:.5px}
.header-catch{position:absolute;top:14px;left:170px;color:var(--yellow);font-weight:900;font-size:15px}
.header-badge{position:absolute;top:7px;left:540px;width:58px;height:34px;background:var(--yellow);color:var(--black);font-size:6px;font-weight:700;text-align:center;line-height:10px;padding-top:2px}
.header-tel{position:absolute;top:6px;left:606px;color:#fff;font-size:5px;line-height:8px}
.header-tel strong{display:block;color:var(--yellow);font-family:"Oswald",sans-serif;font-size:12px;line-height:14px}

/* nav */
.global-nav{position:absolute;top:48px;left:0;width:730px;height:14px;background:var(--dark);display:flex;padding-left:60px}
.global-nav a{color:#fff;font-size:5.5px;text-decoration:none;width:48px;text-align:center;line-height:14px;border-right:1px solid #444}
.global-nav a.current{background:var(--yellow);color:var(--black);font-weight:700}

/* hero */
.hero{position:absolute;top:62px;left:0;width:730px;height:298px;background:linear-gradient(120deg,#f3f3f3 0%,#dcdcdc 45%,#e9e4e4 60%,#c9d2e4 100%)}
.search{position:absolute;top:2px;left:146px;width:340px;height:16px;background:#fff;border:1px solid #bbb}
.search-btn{position:absolute;top:2px;left:490px;width:52px;height:16px;background:var(--dark);color:#fff;font-size:6px;text-align:center;line-height:16px}
.guest{position:absolute;top:2px;left:560px;width:140px;height:16px;background:var(--dark);color:#fff;font-size:6px;text-align:center;line-height:16px}
.dropdown{position:absolute;top:18px;left:146px;width:180px;background:#fff;border:1px solid #ccc;box-shadow:0 2px 4px rgba(0,0,0,.2);z-index:2}
.dropdown li{list-style:none;font-size:5.5px;padding:3px 6px;border-bottom:1px solid #eee}
.news{position:absolute;top:35px;left:134px;width:474px;height:243px;background:#fff;box-shadow:0 0 6px rgba(0,0,0,.15);padding:50px 18px 0}
.news-item{display:flex;gap:12px;border-bottom:1px solid #ddd;padding:8px 0 10px}
.news-date{width:40px;font-size:5.5px;color:#666}
.news-body{flex:1}
.news-title{font-size:6px;font-weight:700;margin-bottom:4px}
.news-text{font-size:5.5px;line-height:9px;color:#555}
.news-thumb{width:90px;height:46px;background:linear-gradient(90deg,#c23 0%,#eee 50%,#23a 100%)}

/* promo band */
.promo{position:absolute;top:360px;left:0;width:730px;height:235px;background:linear-gradient(90deg,#1a1a1a,#2b2b2b 50%,#121212)}
.promo-silhouette{position:absolute;top:100px;left:40px;width:120px;height:110px;background:linear-gradient(180deg,#e6e6e6,#bdbdbd)}
.promo-banner{position:absolute;top:40px;left:231px;width:389px;height:190px;background:#fff;border:3px solid var(--yellow)}
.promo-title{background:var(--black);color:var(--yellow);font-size:11px;font-weight:900;text-align:center;padding:6px 0}
.promo-title span{color:#fff}
.promo-goods{position:absolute;top:48px;left:10px;width:365px;height:86px;background:linear-gradient(90deg,#c62828,#1e3a8a 35%,#e9e9e9 60%,#b0b0b0)}
.promo-circle{position:absolute;top:52px;right:10px;width:58px;height:58px;border-radius:50%;background:var(--yellow);font-size:6px;font-weight:700;text-align:center;padding-top:14px;line-height:9px}
.promo-foot{position:absolute;bottom:8px;left:10px;right:10px;font-size:6px;line-height:10px;border-top:1px solid #ddd;padding-top:6px}

/* recommended */
.recommend{position:absolute;top:595px;left:0;width:730px;height:328px;background:#fff}
.stripe{position:absolute;left:0;width:730px;height:8px;background:var(--black)}
.rec-figure-r{position:absolute;top:40px;left:590px;width:110px;height:66px;background:linear-gradient(90deg,var(--photo-red),var(--photo-blue))}
.rec-figure-l{position:absolute;top:170px;left:8px;width:80px;height:120px;background:linear-gradient(180deg,var(--photo-red),#2a2a2a)}
.rec-heading{position:absolute;top:85px;left:0;width:730px;text-align:center;font-size:13px;font-weight:900;color:var(--black)}
.rec-heading i{display:inline-block;width:12px;height:12px;border-radius:50%;background:var(--yellow);vertical-align:-1px;margin-right:4px}
.cards{position:absolute;top:118px;left:97px;display:flex;gap:12px}
.card{width:140px;background:#fff;border:1px solid #ddd;position:relative;z-index:1}
.card-img{height:95px;background:#ececec}
.card-name{font-size:5.5px;padding:4px 5px;line-height:8px}
.card-price{font-size:8px;color:var(--red);font-weight:700;padding:0 5px 5px}
.card-price small{font-size:5px;color:#555}
.tag{display:inline-block;background:var(--yellow);color:var(--black);font-size:5px;padding:1px 4px;margin-left:5px}

/* strip */
.strip{position:absolute;top:923px;left:0;width:730px;height:37px;background:var(--gray);color:#ddd;text-align:center;font-size:7px;line-height:37px}

/* contact */
.contact{position:absolute;top:960px;left:0;width:730px;height:140px;background:linear-gradient(90deg,#1b1b1b,#3d3d3d 60%,#262626)}
.contact-box{position:absolute;top:8px;left:218px;width:486px;height:124px;background:#fff;display:flex}
.contact-col{padding:10px 8px;border-right:1px solid #ddd}
.contact-col h3{font-size:7px;font-weight:900;margin-bottom:6px}
.tel-box{background:var(--yellow);font-family:"Oswald",sans-serif;font-size:14px;color:var(--black);padding:3px 8px;display:flex;align-items:center;gap:4px}
.contact-col p{font-size:5.5px;line-height:9px;margin-top:5px}
.net-badge{display:inline-block;background:var(--black);color:var(--yellow);font-size:7px;font-weight:700;padding:3px 6px}
.shop-name{font-size:14px;font-weight:900;color:var(--black)}
.contact-btn{display:block;background:var(--yellow);font-size:6px;font-weight:700;text-align:center;padding:5px;margin-top:8px}

/* brands & footer */
.brands{position:absolute;top:1100px;left:0;width:730px;height:40px;background:#fff;display:flex;justify-content:center;align-items:center;gap:40px}
.brands span{font-weight:900;font-size:15px;color:var(--black)}
.site-footer{position:absolute;top:1140px;left:0;width:730px;height:60px;background:var(--dark)}
.footer-nav{display:flex;justify-content:center;gap:18px;padding-top:14px}
.footer-nav a{color:#ddd;font-size:5.5px;text-decoration:none}
.copyright{text-align:center;color:#888;font-size:5px;margin-top:18px}
</style>
</head>
<body>

<header class="site-header">
  <div class="header-topline">レスリング用品専門店 森田スポーツ | 全国配送対応</div>
  <div class="brand"><span class="brand-dot"></span><span class="brand-name">Morita Sports</span></div>
  <div class="brand-sub">WRESTLING SHOP</div>
  <div class="header-catch">小学生から有名選手まで幅広く対応可能！</div>
  <div class="header-badge">客様相談<br>24時間<br>ご予約受付</div>
  <div class="header-tel">ご注文・お問い合わせ<strong>06-4820-3157</strong></div>
</header>

<nav class="global-nav">
  <a class="current">ホーム</a><a>新着商品</a><a>ユニフォーム</a><a>シューズ</a><a>サポーター</a><a>練習用品</a><a>大会情報</a><a>お問い合わせ</a>
</nav>

<section class="hero" role="img" aria-label="試合中のレスリング選手のメイン写真">
  <div class="search"></div>
  <div class="search-btn">検索</div>
  <div class="guest">ようこそゲストさん</div>
  <ul class="dropdown">
    <li>カテゴリーから探す</li><li>シングレット</li><li>レスリングシューズ</li><li>サポーター・小物</li>
  </ul>
  <div class="news">
    <div class="news-item">
      <div class="news-date">2019.9.1</div>
      <div class="news-body">
        <div class="news-title">秋の新作シューズ入荷のお知らせ</div>
        <div class="news-text">人気モデルの新色が入荷しました。サイズは豊富にご用意しております。店頭と通販の両方でご購入いただけます。お早めにご来店ください。</div>
      </div>
    </div>
    <div class="news-item">
      <div class="news-date">2019.8.20</div>
      <div class="news-body">
        <div class="news-title">全国大会に向けた特別セール開催</div>
        <div class="news-text">期間中はユニフォームと練習用品がお得な価格です。チーム単位のご注文も承ります。</div>
      </div>
      <div class="news-thumb" role="img" aria-label="赤と青のシングレットの選手写真"></div>
    </div>
    <div class="news-item">
      <div class="news-date">2019.8.1</div>
      <div class="news-body"><div class="news-title">夏季休業日のご案内を掲載しました</div></div>
    </div>
  </div>
</section>

<section class="promo">
  <div class="promo-silhouette" role="img" aria-label="レスリング選手のシルエット"></div>
  <div class="promo-banner">
    <div class="promo-title">レスリング関連商品<span>は当社にお任せください。</span></div>
    <div class="promo-goods" role="img" aria-label="ユニフォームとシューズの商品写真"></div>
    <div class="promo-circle">本格競技品<br>多数<br>取り扱い</div>
    <div class="promo-foot">競技用からトレーニング用まで幅広く取り揃え。<br>大会に向けたチームオーダーもお気軽にご相談ください。</div>
  </div>
</section>

<section class="recommend">
  <div class="stripe" style="top:40px"></div>
  <div class="stripe" style="top:52px"></div>
  <div class="stripe" style="top:200px"></div>
  <div class="rec-figure-r" role="img" aria-label="組み合うレスリング選手の写真"></div>
  <div class="rec-figure-l" role="img" aria-label="構えるレスリング選手の写真"></div>
  <h2 class="rec-heading"><i></i>オススメ商品</h2>
  <div class="cards">
    <div class="card"><div class="card-img" role="img" aria-label="ニーサポーターの商品写真"></div><div class="card-name">ニーサポーター<br>競技用・左右兼用</div><div class="card-price">3,080<small> 円(税込)</small></div></div>
    <div class="card"><div class="card-img" role="img" aria-label="レスリングシューズの商品写真"></div><div class="card-name">レスリングシューズ<br>軽量モデル</div><div class="card-price">4,990<small> 円(税込)</small><span class="tag">NEW</span></div></div>
    <div class="card"><div class="card-img" role="img" aria-label="赤いシングレットの商品写真"></div><div class="card-name">シングレット 赤<br>公式試合対応</div><div class="card-price">4,990<small> 円(税込)</small><span class="tag">NEW</span></div></div>
    <div class="card"><div class="card-img" role="img" aria-label="青いシングレットの商品写真"></div><div class="card-name">シングレット 青<br>公式試合対応</div><div class="card-price">4,990<small> 円(税込)</small></div></div>
  </div>
</section>

<div class="strip">レスリング商品取扱いはスポーツショップ 森田スポーツ</div>

<section class="contact" role="img" aria-label="練習場の背景写真">
  <div class="contact-box">
    <div class="contact-col" style="width:170px">
      <h3>ご注文・商品お問い合わせ</h3>
      <div class="tel-box"><svg width="10" height="10" viewBox="0 0 24 24"><path fill="#111" d="M6.6 10.8a15 15 0 006.6 6.6l2.2-2.2a1 1 0 011-.25 11 11 0 003.6.6 1 1 0 011 1V20a1 1 0 01-1 1A17 17 0 013 4a1 1 0 011-1h3.5a1 1 0 011 1 11 11 0 00.6 3.6 1 1 0 01-.25 1z"/></svg>06-4820-3157</div>
      <p>営業時間 10:00〜19:00（水曜定休）</p>
    </div>
    <div class="contact-col" style="width:170px">
      <h3>インターネットでのご注文</h3>
      <span class="net-badge">24時間受付</span>
      <p>配達全国対応<br>通販サイトから簡単にご注文いただけます。</p>
    </div>
    <div class="contact-col" style="flex:1;border-right:0">
      <div class="shop-name">森田スポーツ</div>
      <p>〒000-0000 大阪府架空市中央1-2-3</p>
      <span class="contact-btn">お問い合わせはこちら</span>
    </div>
  </div>
</section>

<div class="brands"><span>ARVEN</span><span>KORVA</span></div>

<footer class="site-footer">
  <nav class="footer-nav"><a>ホーム</a><a>新着商品</a><a>ユニフォーム</a><a>シューズ</a><a>サポーター</a><a>練習用品</a><a>大会情報</a><a>お問い合わせ</a></nav>
  <div class="copyright">Copyright © Morita Sports All Rights Reserved.</div>
</footer>

</body>
</html>
```